Online ticketing company needs new biz card design

Needing an updated business card to reflect our company, incorporating our existing logo and colour scheme (red, black, white). The design should communicate our modern, online, technology, innovation based company.

Details for card need to include the following:

Name
Position
Telephone and extension number
Mobile number
Email
Web address
Physical and/or postal address

Industry/Entity Type

Business

Font styles to use
Sans Serif

Requirements
Must have
• Clear, bold, eye catching design

```html
<!DOCTYPE html>
<html lang="en">
<head>
<meta charset="utf-8">
<title>Tixora Business Card</title>
<link rel="stylesheet" href="https://fonts.googleapis.com/css2?family=Lato:wght@400;700;900&display=swap">
<style>
  :root {
    --brand-red: #cc2229;
    --ink: #111111;
    --paper: #ffffff;
    --stage: #e4e4e4;
    --text: #1a1a1a;
  }
  * { box-sizing: border-box; margin: 0; padding: 0; }
  html, body { width: 1200px; height: 1000px; overflow: hidden; }
  body {
    background: var(--stage);
    font-family: "Lato", Arial, sans-serif;
    position: relative;
  }
  .card {
    position: absolute;
    width: 700px;
    height: 400px;
    overflow: hidden;
    box-shadow: 0 6px 18px rgba(0,0,0,0.25);
  }
  /* Back side */
  .card-back {
    left: 80px;
    top: 70px;
    background: var(--brand-red);
  }
  .card-back .corner-stripe {
    position: absolute;
    inset: 0;
    width: 100%;
    height: 100%;
  }
  .card-back .brand-mark {
    position: absolute;
    left: 0;
    top: 0;
    width: 470px;
    height: 400px;
    display: flex;
    align-items: center;
    justify-content: center;
    font-weight: 900;
    font-size: 92px;
    letter-spacing: 2px;
    color: var(--ink);
  }
  /* Front side */
  .card-front {
    left: 420px;
    top: 520px;
    background: var(--paper);
  }
  .card-front .bottom-band {
    position: absolute;
    left: 0;
    bottom: 0;
    width: 100%;
    height: 62px;
    background: var(--brand-red);
    border-top: 8px solid var(--ink);
  }
  .card-front .brand-mark {
    position: absolute;
    left: 40px;
    top: 120px;
    width: 300px;
    text-align: center;
    font-weight: 900;
    font-size: 64px;
    letter-spacing: 1px;
    color: var(--ink);
  }
  .identity {
    position: absolute;
    right: 40px;
    top: 42px;
    text-align: right;
  }
  .identity .person-name {
    font-weight: 700;
    font-size: 26px;
    letter-spacing: 1px;
    color: var(--text);
  }
  .identity .person-title {
    font-weight: 700;
    font-size: 19px;
    color: var(--brand-red);
    margin-top: 2px;
  }
  .contact-list {
    position: absolute;
    right: 40px;
    top: 126px;
    list-style: none;
  }
  .contact-list li {
    display: flex;
    align-items: center;
    justify-content: flex-end;
    gap: 12px;
    height: 36px;
    font-size: 18px;
    color: var(--text);
  }
  .contact-list svg { width: 26px; height: 26px; flex: none; }
  .address {
    position: absolute;
    right: 40px;
    top: 270px;
    text-align: right;
    font-size: 19px;
    line-height: 1.2;
    color: var(--text);
  }
  .address .company {
    font-weight: 700;
    color: var(--brand-red);
  }
</style>
</head>
<body>

<section class="card card-back">
  <svg class="corner-stripe" viewBox="0 0 700 400" aria-hidden="true">
    <polygon points="540,400 700,120 700,400" fill="#ffffff"/>
    <polygon points="556,400 700,148 700,400" fill="#111111"/>
  </svg>
  <div class="brand-mark">TIXORA</div>
</section>

<section class="card card-front">
  <div class="brand-mark">TIXORA</div>

  <div class="identity">
    <div class="person-name">YOUR NAME</div>
    <div class="person-title">Title</div>
  </div>

  <ul class="contact-list">
    <li>123 456 7890
      <svg viewBox="0 0 26 26" aria-hidden="true"><circle cx="13" cy="13" r="13" fill="#cc2229"/><path d="M9 7l3 0 1 4-2 1c1 2 2 3 4 4l1-2 4 1 0 3c-6 1-12-5-11-11z" fill="#fff"/></svg>
    </li>
    <li>123 456 7890
      <svg viewBox="0 0 26 26" aria-hidden="true"><circle cx="13" cy="13" r="13" fill="#cc2229"/><rect x="9" y="6" width="8" height="14" rx="1.5" fill="#fff"/><rect x="10.5" y="8" width="5" height="8" fill="#cc2229"/></svg>
    </li>
    <li>name@tixora.co.nz
      <svg viewBox="0 0 26 26" aria-hidden="true"><circle cx="13" cy="13" r="13" fill="#cc2229"/><rect x="7" y="9" width="12" height="8" fill="#fff"/><path d="M7 9l6 5 6-5" fill="none" stroke="#cc2229" stroke-width="1.2"/></svg>
    </li>
    <li>www.tixora.co.nz
      <svg viewBox="0 0 26 26" aria-hidden="true"><circle cx="13" cy="13" r="13" fill="#cc2229"/><g fill="none" stroke="#fff" stroke-width="1.3"><circle cx="13" cy="13" r="6.5"/><ellipse cx="13" cy="13" rx="3" ry="6.5"/><path d="M6.5 13h13M8 9.5h10M8 16.5h10"/></g></svg>
    </li>
  </ul>

  <div class="address">
    <div class="company">TIXORA</div>
    <div>St. 48 Harbourview, New Zealand</div>
    <div>NZ 4521</div>
  </div>

  <div class="bottom-band"></div>
</section>

</body>
</html>
```